Diversity report of banking market in Europe

*Power point presentation style - rather than corporate brochure*
We are an executive recruitment firm who will be sending a report to all our senior clients. We need a designer to make it look eye catching, slick and professional for our audience. The document will be read mainly by PDF so the type of font and size will be very important as will the size of each page.

We have all the content but may need guidance on the amount of text, the size of graphs and inserting some pictures/vectors etc. We can provide more text or cut text back it it helps the design. We can find more graphs if this helps to fill a page

Industry/Entity Type

Investment Banking

Font styles to use
Sans Serif

Colors
0255a3
33b8a4
85cae6
cfeae6
ffffff

Requirements
Must have
• Colours:
11, 29, 49
70, 165, 175
Nice to have
• Have added two example Varnholt documents that we feel are clean and professional. Please use these are our attempt as a guide line to how was want the document to look and feel and flow. Happy to add additional pictures or design to fill out pages. Cant steal actual pictures from varnholt report

```html
<!DOCTYPE html>
<html lang="en">
<head>
<meta charset="utf-8">
<title>Diversity report of banking market in Europe</title>
<link href="https://fonts.googleapis.com/css2?family=Montserrat:wght@400;500&family=Bebas+Neue&family=Barlow:wght@400;600&family=Cinzel:wght@400&display=swap" rel="stylesheet">
<style>
  :root{
    --board:#ebebeb;
    --ink:#111111;
    --heading-grey:#55585c;
    --accent-blue:#0c9fc2;
    --teal:#33b8a4;
    --panel:#d2ecf1;
    --spread:#f4f9fa;
    --sky-top:#8ccbea;
    --sky-mid:#4f95c4;
    --sky-deep:#0b1d31;
    --white:#ffffff;
    --body:#2a2d30;
  }
  *{margin:0;padding:0;box-sizing:border-box}
  html,body{width:1200px;height:1200px;overflow:hidden;background:var(--board)}
  .board{position:relative;width:1200px;height:1200px;font-family:"Barlow",sans-serif;color:var(--ink)}
  .board-title{position:absolute;left:125px;top:84px;font-family:"Montserrat",sans-serif;font-weight:500;font-size:26px;letter-spacing:.2px}

  /* cover */
  .cover{position:absolute;left:146px;top:350px;width:316px;height:316px;overflow:hidden}
  .cover-photo{position:absolute;inset:0;background:linear-gradient(180deg,var(--sky-top) 0%,var(--sky-mid) 55%,var(--sky-deep) 100%)}
  .cover-brand{position:absolute;left:24px;top:14px;font-family:"Cinzel",serif;font-size:11px;color:#1d2a38;letter-spacing:.5px}
  .cover-title{position:absolute;left:24px;top:64px;font-family:"Bebas Neue",sans-serif;font-weight:400;font-size:23px;line-height:24px;color:#3a4650}
  .cover-sub{position:absolute;left:24px;top:114px;font-size:7px;line-height:9.5px;color:#1d2a38}
  .cover-author{position:absolute;left:122px;top:294px;font-size:6px;font-weight:600;color:var(--white);border-bottom:1px solid var(--white);padding-bottom:1px}

  /* spread */
  .spread{position:absolute;left:146px;top:676px;width:948px;height:316px;background:var(--spread)}
  .page-num{position:absolute;font-family:"Bebas Neue",sans-serif;font-size:50px;line-height:1;color:var(--heading-grey)}
  .page-bar{position:absolute;width:22px;height:5px;background:var(--accent-blue)}
  .title-box{position:absolute;background:var(--panel);padding:16px 7px;overflow:hidden}
  .title-box h2{font-family:"Bebas Neue",sans-serif;font-weight:400;color:var(--heading-grey);font-size:32px;line-height:29px}
  .title-box.long h2{font-size:26px;line-height:25px;letter-spacing:-.2px}
  .title-box p{font-size:4.6px;line-height:5.7px;color:var(--body);margin-top:9px}
  .body-col{position:absolute;font-size:4.6px;line-height:5.6px;color:var(--body);text-align:justify}
  .body-col p+p{margin-top:6px}

  .stats{position:absolute;left:325px;top:31px;width:277px;height:250px;background:var(--panel)}
  .stats .intro{position:absolute;left:15px;top:8px;width:247px;font-size:4.3px;line-height:5.5px;color:var(--body);text-align:justify}
  .stats .intro p+p{margin-top:5px}
  .stat-label{position:absolute;font-family:"Bebas Neue",sans-serif;color:var(--teal);font-size:15px;line-height:1}
  .stat-value{position:absolute;font-family:"Bebas Neue",sans-serif;color:var(--teal);font-size:32px;line-height:1}
  .stat-note{position:absolute;font-size:4.4px;line-height:5.5px;color:var(--body);width:105px}
  .people{position:absolute;left:101px;top:82px;width:82px;height:82px}
  .donut{position:absolute;width:42px;height:42px}
</style>
</head>
<body>
<main class="board">
  <h1 class="board-title">Diversity report of banking market in Europe</h1>

  <section class="cover">
    <div class="cover-photo" role="img" aria-label="Photograph looking up a glass office tower against a clear blue sky"></div>
    <div class="cover-brand">Halden Grove</div>
    <h2 class="cover-title">Diversity Review<br>in Corporate Credit</h2>
    <p class="cover-sub">Gender &amp; Ethnicity within Credit Investment<br>Management &amp; Leveraged Finance</p>
    <p class="cover-author">Written by Lena Marsh</p>
  </section>

  <section class="spread">
    <!-- page 1 -->
    <div class="page-num" style="left:50px;top:28px">1</div>
    <div class="page-bar" style="left:48px;top:72px"></div>
    <div class="title-box" style="left:36px;top:114px;width:106px;height:164px">
      <h2>Intro-<br>duction</h2>
      <p>Gender remains a central theme across asset management, and public attention on fair hiring is pushing firms to act, close gaps and report openly on the make-up of their teams at every level.</p>
    </div>
    <div class="body-col" style="left:150px;top:114px;width:154px">
      <p>Diversity reviews in the press focus mainly on senior staff and boards, leaving the make-up of investment teams largely unseen. Below board level the numbers are far less transparent, and firms are now asking for a clear view of where they stand across mid and junior grades.</p>
      <p>In this report we analyse the figures and draw conclusions where the data allows, while leaving room for readers to form their own view. The aim is to show what the market truly looks like today.</p>
      <p>We also review the pipeline that feeds the industry, comparing university intake with the make-up of investment teams, so senior leaders can judge progress against a fair and consistent benchmark.</p>
    </div>

    <!-- stats page -->
    <div class="stats">
      <div class="intro">
        <p>This report builds on a long track record in credit, allowing us to break the numbers down line by line and share the hard data behind each finding. We reviewed teams across direct lending, distressed debt, CLOs and special situations, alongside leveraged finance.</p>
        <p>Gender levels across each strategy are explored further below. The chart shows the ratio of male to female investment professionals, with direct lending holding the closest ratio.</p>
      </div>
      <div class="stat-label" style="left:20px;top:92px">Direct Lending</div>
      <div class="stat-value" style="left:22px;top:112px">17%</div>
      <svg class="people" viewBox="0 0 82 82" role="img" aria-label="Illustration of a man and a woman inside a circular arrow">
        <circle cx="41" cy="41" r="39" fill="none" stroke="#33b8a4" stroke-width="1"/>
      </svg>
      <div class="stat-label" style="left:196px;top:92px">Banking</div>
      <div class="stat-value" style="left:229px;top:112px">14%</div>
      <p class="stat-note" style="left:19px;top:187px">Professionals tracked across direct lending, distressed debt and CLOs in Europe, of whom a minority are female.</p>
      <p class="stat-note" style="left:135px;top:187px;width:130px">Investment professionals across lending and leveraged finance identify as ethnic minorities, the rest as white.</p>
      <svg class="donut" style="left:53px;top:204px" viewBox="0 0 42 42"><circle cx="21" cy="21" r="16" fill="none" stroke="#dcdcdc" stroke-width="7"/><circle cx="21" cy="21" r="16" fill="none" stroke="#33b8a4" stroke-width="7" stroke-dasharray="83.5 100.5" transform="rotate(-59 21 21)"/></svg>
      <svg class="donut" style="left:208px;top:204px" viewBox="0 0 42 42"><circle cx="21" cy="21" r="16" fill="none" stroke="#dcdcdc" stroke-width="7"/><circle cx="21" cy="21" r="16" fill="none" stroke="#33b8a4" stroke-width="7" stroke-dasharray="86.4 100.5" transform="rotate(-50 21 21)"/></svg>
    </div>

    <!-- page 2 -->
    <div class="page-num" style="left:682px;top:28px">2</div>
    <div class="page-bar" style="left:680px;top:72px"></div>
    <div class="title-box long" style="left:668px;top:114px;width:108px;height:164px">
      <h2>Gender<br>Diversity<br>Across<br>All<br>Strategies</h2>
    </div>
    <div class="body-col" style="left:782px;top:114px;width:154px">
      <p>Diversity reviews in the press focus mainly on senior staff and boards, leaving the make-up of investment teams largely unseen. Below board level the numbers are far less transparent, and firms are now asking for a clear view of where they stand across mid and junior grades.</p>
      <p>In this report we analyse the figures and draw conclusions where the data allows, while leaving room for readers to form their own view. The aim is to show what the market truly looks like today.</p>
      <p>We also review the pipeline that feeds the industry, comparing university intake with the make-up of investment teams, so senior leaders can judge progress against a fair and consistent benchmark.</p>
    </div>
  </section>
</main>
</body>
</html>
```